Recycling Depot Business Card Design

We need a double sided business card for our recycling depot business. Please include name, position, address, phone, cell, fax, email and website address. Business card should match the colour scheme of our logo and look environmental but modern. I've attached a few business cards from Mintvale Works that I like.

Industry/Entity Type

Recycling

Contact Information for Business Card

Please include name, position, address, phone, cell, fax, email and website address.

Font styles to use
Sans Serif

Requirements
Must have
• Our Logo, Colour Scheme that matches our logo. Use of Colour Gradients and a custom look.

```html
<!DOCTYPE html>
<html lang="en">
<head>
<meta charset="utf-8">
<title>Greenloop Depot – Business Card</title>
<link rel="stylesheet" href="https://fonts.googleapis.com/css2?family=Lato:wght@400;700&display=swap">
<style>
  :root {
    --bg: #6b7176;
    --card-white: #ffffff;
    --green-dark: #1e6b34;
    --green-light: #6bbf3c;
    --green-back: #1f6835;
    --text-grey: #555a5c;
    --shadow: rgba(0, 0, 0, 0.35);
  }
  * { margin: 0; padding: 0; box-sizing: border-box; }
  html, body { width: 1200px; height: 807px; overflow: hidden; }
  body {
    position: relative;
    background: var(--bg);
    font-family: "Lato", sans-serif;
  }
  .card {
    position: absolute;
    border-radius: 22px;
    box-shadow: 3px 4px 8px var(--shadow);
  }
  .card-front { left: 341px; top: 81px; width: 517px; height: 296px; background: var(--card-white); }
  .card-back  { left: 347px; top: 430px; width: 506px; height: 289px; background: var(--green-back); }

  .brand {
    position: absolute;
    display: flex;
    align-items: center;
    gap: 12px;
    font-family: "Lato", sans-serif;
    font-weight: 700;
    font-size: 40px;
    line-height: 1;
    white-space: nowrap;
  }
  .brand-mark { width: 30px; height: 30px; border-radius: 50%; flex: none; }
  .card-front .brand { left: 90px; top: 66px; color: var(--green-dark); }
  .card-front .brand-mark { background: var(--green-light); }
  .card-back .brand { left: 86px; top: 124px; color: #ffffff; }
  .card-back .brand-mark { background: var(--green-light); }

  .person {
    position: absolute;
    right: 287px;
    top: 177px;
    text-align: right;
    color: var(--text-grey);
  }
  .person-name { font-weight: 700; font-size: 23px; letter-spacing: 0.2px; line-height: 1; }
  .person-name .first { color: var(--green-dark); }
  .person-name .last { color: var(--green-light); }
  .person-role { font-size: 12px; margin-top: 8px; }
  .person-address { font-size: 12px; margin-top: 9px; line-height: 16.5px; }

  .divider {
    position: absolute;
    left: 259px; top: 177px;
    width: 1px; height: 82px;
    background: var(--green-dark);
  }

  .contacts {
    position: absolute;
    left: 287px; top: 172px;
    list-style: none;
    color: var(--text-grey);
    font-size: 14.5px;
  }
  .contacts li { display: flex; align-items: center; height: 18.3px; }
  .contacts svg { width: 13px; height: 13px; margin-right: 12px; fill: var(--green-dark); flex: none; }
  .contacts .accent { color: var(--green-dark); }
</style>
</head>
<body>
  <section class="card card-front">
    <div class="brand"><span class="brand-mark"></span>Greenloop Depot</div>

    <div class="person">
      <div class="person-name"><span class="first">AARON</span> <span class="last">VELL</span></div>
      <div class="person-role">Founder &amp; CEO</div>
      <div class="person-address">1234 First Line Address<br>5678 Second Line Address</div>
    </div>

    <div class="divider"></div>

    <ul class="contacts">
      <li><svg viewBox="0 0 16 16"><path d="M1 5c0-2 3-3 7-3s7 1 7 3v1h-3V4.5H4V6H1zM3 7h10l1 7H2zm5 1.5a2 2 0 1 0 0 4 2 2 0 0 0 0-4z"/></svg>+ 100 8888 0000</li>
      <li><svg viewBox="0 0 16 16"><path d="M4 0h8a1 1 0 0 1 1 1v14a1 1 0 0 1-1 1H4a1 1 0 0 1-1-1V1a1 1 0 0 1 1-1zm1 2v10h6V2zm3 11a1 1 0 1 0 0 2 1 1 0 0 0 0-2z"/></svg>+ 100 8888 0000</li>
      <li><svg viewBox="0 0 16 16"><path d="M4 0h8v4H4zM1 5h14v7h-3v-3H4v3H1zm4 5h6v6H5z"/></svg>+ 100 8888 0000</li>
      <li><svg viewBox="0 0 16 16"><path d="M0 3h16v10H0zm1.5 1.2L8 9l6.5-4.8M1.5 12l4.5-4M14.5 12L10 8" stroke="#fff" stroke-width="1"/></svg>info@greenloopdepot.com</li>
      <li><svg viewBox="0 0 16 16"><path d="M8 0a8 8 0 1 0 0 16A8 8 0 0 0 8 0zm0 1.2a6.8 6.8 0 1 1 0 13.6A6.8 6.8 0 0 1 8 1.2zM7.4 2v12h1.2V2zM2 7.4h12v1.2H2zM3 4.5h10v1H3zm0 6h10v1H3z"/></svg>www.<span class="accent">greenloopdepot</span>.com</li>
    </ul>
  </section>

  <section class="card card-back">
    <div class="brand"><span class="brand-mark"></span>Greenloop Depot</div>
  </section>
</body>
</html>
```